Business Card Design

We are a non profit organization that holds 10 days of races and car shows to raise money for autism. We stage the largest vintage race event in the country and the only one held on city streets.

We need business cards for myself and for 100 volunteers that stage the event. We like our cards to look exciting and to capture the essence of vintage racing.

Target Market(s)

sponsors and volunteers - most in the auto industry. This is not a TORVEX crowd

Industry/Entity Type

Non Profit

Contact Information for Business Card

Marcus Feldwright
Executive Director
Harborline Classic Motor Rally Association
2750 Kestrel Lane, Suite 214
Pittsburgh, PA 15907
feldwright@hcmra-example.org
cell 412 683-7142
www.hcmra-example.org

Font styles to use
Sans Serif

Colors
ec2027

Requirements
Must have
• our logo place a car image.Could place racing image on back of card along with website

Must include this statement small somewhere:
Benefitting the Brightpath Spectrum Society and Willowmere Ridge School

```html
<!DOCTYPE html>
<html lang="en">
<head>
<meta charset="utf-8">
<title>Harborline Classic Motor Rally – Business Card</title>
<link rel="stylesheet" href="https://fonts.googleapis.com/css2?family=Exo+2:wght@400;500;600&display=swap">
<style>
  :root {
    --race-red: #ec2027;
    --ink: #1a1a1a;
    --muted: #555555;
    --paper: #ffffff;
    --frame: #9a9a9a;
    --card-edge: #b5b5b5;
    --night: #0c0c0c;
  }
  * { box-sizing: border-box; margin: 0; padding: 0; }
  html, body { width: 1140px; height: 1200px; overflow: hidden; }
  body {
    position: relative;
    background: var(--paper);
    border: 2px solid var(--frame);
    font-family: "Exo 2", "Helvetica Neue", Arial, sans-serif;
    color: var(--ink);
  }
  .card {
    position: absolute;
    left: 163px;
    width: 812px;
    background: var(--paper);
    overflow: hidden;
  }
  .card--front { top: 86px; height: 465px; border: 2px solid var(--card-edge); }
  .card--back { top: 647px; height: 461px; }

  .web-band {
    position: absolute;
    left: 0; right: 0;
    height: 44px;
    background: var(--race-red);
    color: var(--paper);
    font-size: 27px;
    font-weight: 500;
    letter-spacing: 0.5px;
    text-align: center;
    line-height: 44px;
  }
  .card--front .web-band { top: 17px; }
  .card--back .web-band { top: 388px; }

  .brand-mark {
    position: absolute;
    left: 86px; top: 130px;
    width: 260px; height: 260px;
    display: flex; align-items: center; justify-content: center;
    text-align: center;
    color: var(--race-red);
    font-size: 27px;
    font-weight: 600;
    line-height: 1.25;
    letter-spacing: 1px;
  }

  .benefit-note {
    position: absolute;
    left: 30px; top: 408px;
    width: 372px;
    text-align: center;
    font-size: 11px;
    line-height: 15px;
    color: var(--muted);
  }

  .divider {
    position: absolute;
    left: 407px; top: 89px;
    width: 3px; height: 355px;
    background: linear-gradient(to bottom, var(--race-red) 0%, var(--race-red) 55%, rgba(236,32,39,0.15) 100%);
  }

  .contact {
    position: absolute;
    left: 452px; top: 96px;
    width: 350px;
  }
  .contact__name { font-size: 20px; font-weight: 500; letter-spacing: 0.6px; }
  .contact__title { font-size: 14px; margin-top: 3px; }
  .contact__address { font-size: 14px; line-height: 28px; margin-top: 76px; }
  .contact__list { list-style: none; margin-top: 28px; }
  .contact__list li {
    display: flex; align-items: center;
    font-size: 14px; height: 35px;
  }
  .contact__list li.small { font-size: 13px; height: 23px; }
  .contact__list svg { width: 15px; height: 15px; margin-right: 12px; fill: var(--ink); flex: none; }

  .race-photo {
    position: absolute;
    left: 0; top: 0;
    width: 100%; height: 388px;
    background: linear-gradient(to bottom, #6f8a4a 0%, #8a9a5a 28%, #6b6e58 55%, #8c8c86 72%, #3e3f38 100%);
  }
  .night-strip {
    position: absolute;
    left: 0; bottom: 0;
    width: 100%; height: 29px;
    background: var(--night);
  }
</style>
</head>
<body>
  <section class="card card--front" aria-label="Business card front">
    <div class="web-band">www.hcmra-example.org</div>
    <div class="brand-mark">HARBORLINE<br>CLASSIC<br>MOTOR RALLY</div>
    <p class="benefit-note">Benefitting the Brightpath Spectrum Society<br>and Willowmere Ridge School</p>
    <div class="divider"></div>
    <div class="contact">
      <p class="contact__name">MARCUS FELDWRIGHT</p>
      <p class="contact__title">Executive Director</p>
      <p class="contact__address">2750 Kestrel Lane, Suite 214<br>Pittsburgh, PA 15907</p>
      <ul class="contact__list">
        <li><svg viewBox="0 0 24 24" aria-hidden="true"><path d="M6.6 10.8a15 15 0 0 0 6.6 6.6l2.2-2.2c.3-.3.7-.4 1-.2 1.1.4 2.3.6 3.6.6.6 0 1 .4 1 1V20c0 .6-.4 1-1 1A17 17 0 0 1 3 4c0-.6.4-1 1-1h3.5c.6 0 1 .4 1 1 0 1.3.2 2.5.6 3.6.1.3 0 .7-.2 1z"/></svg>412 683-7142</li>
        <li><svg viewBox="0 0 24 24" aria-hidden="true"><path d="M7 1h10a2 2 0 0 1 2 2v18a2 2 0 0 1-2 2H7a2 2 0 0 1-2-2V3a2 2 0 0 1 2-2zm0 3v14h10V4zm5 15.5a1.2 1.2 0 1 0 0 2.4 1.2 1.2 0 0 0 0-2.4z"/></svg>412 683-7142</li>
        <li><svg viewBox="0 0 24 24" aria-hidden="true"><path d="M7 2h8l3 3v5H7zM4 11h16a2 2 0 0 1 2 2v7H2v-7a2 2 0 0 1 2-2zm3 3v2h2v-2zm4 0v2h2v-2zm4 0v2h2v-2z"/></svg>412 683-7142</li>
        <li class="small"><svg viewBox="0 0 24 24" aria-hidden="true"><path d="M2 5h20v14H2zm2 2v.5l8 5 8-5V7z"/></svg>feldwright@hcmra-example.org</li>
        <li class="small"><svg viewBox="0 0 24 24" aria-hidden="true"><path d="M12 2a10 10 0 1 0 0 20 10 10 0 0 0 0-20zm6.9 9h-3a15 15 0 0 0-1.3-5.6A8 8 0 0 1 18.9 11zM12 4c.9 1.2 1.8 3.6 1.9 7h-3.8c.1-3.4 1-5.8 1.9-7zM9.4 5.4A15 15 0 0 0 8.1 11h-3a8 8 0 0 1 4.3-5.6zM5.1 13h3a15 15 0 0 0 1.3 5.6A8 8 0 0 1 5.1 13zm6.9 7c-.9-1.2-1.8-3.6-1.9-7h3.8c-.1 3.4-1 5.8-1.9 7zm2.6-1.4a15 15 0 0 0 1.3-5.6h3a8 8 0 0 1-4.3 5.6z"/></svg>www.hcmra-example.org</li>
      </ul>
    </div>
  </section>

  <section class="card card--back" aria-label="Business card back">
    <div class="race-photo" role="img" aria-label="Photograph of a white vintage open-wheel race car with yellow wheels speeding along a tree-lined course, a second car following behind"></div>
    <div class="web-band">www.hcmra-example.org</div>
    <div class="night-strip"></div>
  </section>
</body>
</html>
```